Building company buisness cards

We are looking for a sharp modern new look for our business cards.We are a New Zealand based company that specialises in house and land packages.We have attached a photo of the current logo and would like to see if it can be improved somehow if needed.We are open to any colours but we have chosen Black and White at this stage. Feel free to change the font and make the logo smarter looking.Play with the colours and see what looks best.We want a card that looks so good know one will want to throw it away!

Target Market(s)

Building profesonals, home buyers

Industry/Entity Type

Building

Contact Information for Business Card

Derek Haskins
0274930268
derekh@stonerange.co.nz

Font styles to use
Serif
Sans Serif

Colors

Designer to choose colors to be used in the design.

Requirements
Must have
• Just the logo on one side and details on the other
• Clean simple looking card
Nice to have
• Round corners and detail like raised or spot UV
• Something that stands out
Should not have
• To title needed, Director etc

```html
<!DOCTYPE html>
<html lang="en">
<head>
<meta charset="utf-8">
<title>Stonerange Business Cards</title>
<link rel="stylesheet" href="https://fonts.googleapis.com/css2?family=Tinos:wght@700&family=Lato:wght@400&display=swap">
<style>
  :root {
    --backdrop: #212121;
    --card: #efefef;
    --ink: #1d1a1a;
    --emboss-dark: #d9d9d9;
    --emboss-light: #fbfbfb;
  }
  html, body {
    margin: 0;
    padding: 0;
    width: 1200px;
    height: 900px;
    overflow: hidden;
    background: var(--backdrop);
  }
  .stage {
    position: relative;
    width: 1200px;
    height: 900px;
  }
  .card {
    position: absolute;
    top: 200px;
    width: 310px;
    height: 502px;
    background: var(--card);
    overflow: hidden;
  }
  .card--details {
    left: 253px;
    border-radius: 60px 0 0 60px;
  }
  .card--brand {
    left: 627px;
    border-radius: 0 60px 0 60px;
  }
  .details-wordmark {
    position: absolute;
    left: 0;
    top: 155px;
    width: 310px;
    margin: 0;
    text-align: center;
    font-family: "Tinos", "Times New Roman", serif;
    font-weight: 700;
    font-size: 36px;
    line-height: 1;
    color: var(--ink);
    letter-spacing: -0.3px;
  }
  .holder-name {
    position: absolute;
    left: 36px;
    top: 352px;
    margin: 0;
    font-family: "Tinos", "Times New Roman", serif;
    font-weight: 700;
    font-size: 23px;
    color: var(--ink);
    letter-spacing: 0.2px;
  }
  .contact-list {
    position: absolute;
    left: 35px;
    top: 414px;
    margin: 0;
    padding: 0;
    list-style: none;
    font-family: "Lato", Arial, sans-serif;
    font-size: 14px;
    line-height: 19px;
    color: var(--ink);
  }
  .contact-list li {
    display: flex;
    align-items: center;
    gap: 4px;
  }
  .contact-icon {
    width: 11px;
    height: 10px;
    flex: none;
  }
  .emboss-ring {
    position: absolute;
    left: 0;
    top: 0;
  }
  .brand-lockup {
    position: absolute;
    left: 34px;
    top: 208px;
  }
  .brand-name {
    margin: 0;
    font-family: "Tinos", "Times New Roman", serif;
    font-weight: 700;
    font-size: 50px;
    line-height: 1;
    color: var(--ink);
    letter-spacing: -0.5px;
  }
  .brand-tagline {
    margin: 4px 0 0 2px;
    font-family: "Lato", Arial, sans-serif;
    font-size: 12.5px;
    color: var(--ink);
    letter-spacing: 0.3px;
  }
</style>
</head>
<body>
<main class="stage">
  <section class="card card--details">
    <p class="details-wordmark">Stonerange</p>
    <h1 class="holder-name">Derek Haskins</h1>
    <ul class="contact-list">
      <li>
        <svg class="contact-icon" viewBox="0 0 11 10" aria-hidden="true">
          <path d="M1 3.2 C1 1.6 10 1.6 10 3.2 L10 4 L7.6 4 L7.4 3 L3.6 3 L3.4 4 L1 4 Z" fill="var(--ink)"/>
          <path d="M2.6 5 L8.4 5 L9.5 9.4 L1.5 9.4 Z" fill="var(--ink)"/>
          <circle cx="5.5" cy="7" r="1" fill="var(--card)"/>
        </svg>
        <span>0274930268</span>
      </li>
      <li>
        <svg class="contact-icon" viewBox="0 0 11 10" aria-hidden="true">
          <rect x="0.5" y="1.5" width="10" height="7.5" fill="var(--ink)"/>
          <path d="M0.8 2 L5.5 6 L10.2 2" fill="none" stroke="var(--card)" stroke-width="0.9"/>
        </svg>
        <span>derekh@stonerange.co.nz</span>
      </li>
    </ul>
  </section>

  <section class="card card--brand">
    <svg class="emboss-ring" width="310" height="502" viewBox="0 0 310 502" aria-hidden="true">
      <circle cx="170" cy="258" r="204" fill="none" stroke="var(--emboss-dark)" stroke-width="4"/>
      <circle cx="170" cy="260" r="204" fill="none" stroke="var(--emboss-light)" stroke-width="2"/>
    </svg>
    <div class="brand-lockup">
      <p class="brand-name">Stonerange</p>
      <p class="brand-tagline">Homes shaped around you.</p>
    </div>
  </section>
</main>
</body>
</html>
```